Business Card Design Project

I am a psychotherapist, counselor and expressive arts therapist (means I use every art form imaginable in the service of healing). I'm just starting out in private practice in San Francisco, CA. I work with individual adults, children and families. I'd like the card to mirror the simplicity and color palate of my website. I also would love if there is a symbol, image of fire, flame or spark (that is warming, not frightening).

Check out my website: www.lorabeckettmft.com

I want the cards to be printed in letter press so please keep that in mind!

Target Market(s)

Upper Middle Class Adults who are progressively minded, artistic or artists, open to psychotherapy, interested in health & healing.

Industry/Entity Type

Business

Requirements
Must have
• Text to be included:

Lora Beckett
Counseling, Psychotherapy & Expressive Arts

2814 Wexford Avenue, Suite F
San Francisco, CA 94127
p. 415.862.3097
lorajanebeckett@mailvane.net

www.lorabeckettmft.com

MFT License Number 68947

It's OK to abbreviate Number to # or Street to St., etc.

Must be compatible with letter press printing.
Nice to have
• I don't have a logo. I don't expect designers to necessarily create one for me, but if someone comes up with a simple image (see above about flame), that would be great. I don't have much of a budget now, but expect that to change in the next year or so and then could buy a logo for my website, future letterhead, etc.

```html
<!DOCTYPE html>
<html lang="en">
<head>
<meta charset="utf-8">
<title>Lora Beckett – Business Cards</title>
<link rel="stylesheet" href="https://fonts.googleapis.com/css2?family=Didact+Gothic&display=swap">
<style>
  :root {
    --backdrop: #3a3d42;
    --card-stock: #e5e5e3;
    --ink-dark: #3f3f3f;
    --ink-red: #d8291e;
    --ink-orange: #e0851a;
  }
  * { margin: 0; padding: 0; box-sizing: border-box; }
  html, body {
    width: 1200px;
    height: 900px;
    overflow: hidden;
  }
  body {
    position: relative;
    background: var(--backdrop);
    font-family: "Didact Gothic", "Century Gothic", sans-serif;
    color: var(--ink-dark);
  }
  .card {
    position: absolute;
    width: 382px;
    height: 675px;
    background: var(--card-stock);
    box-shadow: 0 2px 8px rgba(0, 0, 0, 0.45);
    text-align: center;
  }
  .card--orange { left: 153px; top: 65px; --name-ink: var(--ink-orange); }
  .card--red { left: 590px; top: 172px; --name-ink: var(--ink-red); }

  .card__mark {
    position: absolute;
    left: 0;
    top: 125px;
    width: 100%;
    display: flex;
    flex-direction: column;
    align-items: center;
    gap: 18px;
  }
  .card__mark-dot {
    width: 110px;
    height: 110px;
    border-radius: 50%;
    background: var(--ink-red);
  }
  .card__mark-name {
    font-size: 20px;
    color: var(--ink-red);
    line-height: 1;
  }

  .card__line {
    position: absolute;
    left: 0;
    width: 100%;
    line-height: 1;
    white-space: nowrap;
  }
  .card__name {
    top: 370px;
    font-size: 33px;
    color: var(--name-ink);
  }
  .card__tagline { font-size: 15.5px; }
  .card__tagline--one { top: 410px; }
  .card__tagline--two { top: 430px; }
  .card__contact { font-size: 18px; }
  .card__phone { top: 472px; }
  .card__email { top: 494px; }
  .card__web { top: 517px; }
  .card__address { font-size: 18px; }
  .card__address--one { top: 563px; }
  .card__address--two { top: 586px; }
  .card__license {
    top: 632px;
    font-size: 15px;
  }
</style>
</head>
<body>

  <article class="card card--orange">
    <div class="card__mark">
      <span class="card__mark-dot"></span>
      <span class="card__mark-name">Lora Beckett</span>
    </div>
    <h1 class="card__line card__name">Lora Beckett</h1>
    <p class="card__line card__tagline card__tagline--one">Counseling, Psychotherapy</p>
    <p class="card__line card__tagline card__tagline--two">&amp; Expressive Arts</p>
    <p class="card__line card__contact card__phone">p. 415.862.3097</p>
    <p class="card__line card__contact card__email">lorajanebeckett@mailvane.net</p>
    <p class="card__line card__contact card__web">www.lorabeckettmft.com</p>
    <p class="card__line card__address card__address--one">2814 Wexford Avenue, Suite F</p>
    <p class="card__line card__address card__address--two">San Francisco, CA 94127</p>
    <p class="card__line card__license">MFT License Number 68947</p>
  </article>

  <article class="card card--red">
    <div class="card__mark">
      <span class="card__mark-dot"></span>
      <span class="card__mark-name">Lora Beckett</span>
    </div>
    <h1 class="card__line card__name">Lora Beckett</h1>
    <p class="card__line card__tagline card__tagline--one">Counseling, Psychotherapy</p>
    <p class="card__line card__tagline card__tagline--two">&amp; Expressive Arts</p>
    <p class="card__line card__contact card__phone">p. 415.862.3097</p>
    <p class="card__line card__contact card__email">lorajanebeckett@mailvane.net</p>
    <p class="card__line card__contact card__web">www.lorabeckettmft.com</p>
    <p class="card__line card__address card__address--one">2814 Wexford Avenue, Suite F</p>
    <p class="card__line card__address card__address--two">San Francisco, CA 94127</p>
    <p class="card__line card__license">MFT License Number 68947</p>
  </article>

</body>
</html>
```